Brightleaf Plots LLC business card

I created a front and back idea of what I want. Also I included my Brightleaf Plots logo to be used on the card. Please use your creativity to make it look professional and awesome! Use the all text and phrases in the sample card that I made.

(Front of card)Key words and phrases:
FOOD GROWING MACHINES
Aeroponics Technology
No soil
No pesticides
98% less water
Grow year round

(Back of card)
EVERY MONTH ONE SPIRE PLANTER WILL BE GIVEN AWAY
FOLLOW US ON IG FOR A CHANCE TO WIN A SPIRE PLANTER
FOOD GROWING MACHINES
Vertical Farming
Urban Farming
100% Organic
Grows 40% Faster
Indoors/outdoors

My contact info:
Chef Morv
Phone:555 417-3290
web: brightleafplots.example
IG: brightleafplotsxy

Target Market(s)

urban farming, vertical farming gardening

Industry/Entity Type

Gardening

Contact Information for Business Card

Front of card)Key words and phrases:
FOOD GROWING MACHINES
Aeroponics Technology
No soil
No pesticides
98% less water
Grow year round

(Back of card)
FOOD GROWING MACHINES
Vertical Farming
Urban Farming
100% Organic
Grows 40% Faster
Indoors/outdoors

My contact info:
Phone:555 417-3290
web: brightleafplots.example
IG: brightleafplotsxy

Requirements
Must have
• My contact info:
Chef Morv
Phone:555 417-3290
web: brightleafplots.example
IG: brightleafplotsxy
Nice to have
• Great imagery and easy to read. Try to incorporate the image that I uploaded of the little girl.

```html
<!DOCTYPE html>
<html lang="en">
<head>
<meta charset="utf-8">
<title>Brightleaf Plots – Business Card</title>
<link href="https://fonts.googleapis.com/css2?family=Quicksand:wght@400;500;700&display=swap" rel="stylesheet">
<style>
  :root {
    --canvas-bg: #f1f1f1;
    --brand-blue: #415ead;
    --band-blue: #5670ba;
    --band-dark: #2a2d38;
    --leaf-green: #7dc832;
    --text-white: #ffffff;
    --rule: rgba(255,255,255,0.22);
  }
  * { box-sizing: border-box; margin: 0; padding: 0; }
  html, body {
    width: 1200px; height: 1100px; overflow: hidden;
    background: var(--canvas-bg);
    font-family: "Quicksand", sans-serif;
  }
  .card {
    position: absolute; left: 150px;
    width: 900px; height: 514px;
    background: var(--brand-blue);
    overflow: hidden;
    box-shadow: 0 6px 18px rgba(0,0,0,0.12);
    color: var(--text-white);
  }
  .card--front { top: 24px; }
  .card--back { top: 562px; }

  .card__shapes { position: absolute; inset: 0; }

  .tagline {
    position: absolute; left: 40px; top: 410px;
    font-size: 24px; font-weight: 400; letter-spacing: 1px;
    color: var(--leaf-green);
  }
  .brand-name {
    font-weight: 700; color: var(--leaf-green);
    text-transform: uppercase; line-height: 0.9; letter-spacing: 1px;
  }
  .card--front .brand-name {
    position: absolute; right: 40px; top: 200px;
    font-size: 34px; text-align: right;
  }
  .feature-list { list-style: none; }
  .feature-list--front {
    position: absolute; right: 40px; top: 292px;
    text-align: right;
  }
  .feature-list--front li {
    font-size: 21px; font-weight: 500; line-height: 38px;
    display: flex; justify-content: flex-end; align-items: center; gap: 12px;
  }
  .leaf {
    display: inline-block; width: 18px; height: 18px;
    background: var(--leaf-green);
    border-radius: 0 70% 0 70%;
    flex: none;
  }

  /* back */
  .card--back .brand-name {
    position: absolute; left: 130px; top: 62px;
    font-size: 48px; text-align: center;
  }
  .contact {
    position: absolute; left: 480px; top: 60px;
  }
  .contact__name { font-size: 46px; font-weight: 500; margin-bottom: 10px; }
  .contact__line {
    font-size: 20px; font-weight: 500; line-height: 32px;
    display: flex; align-items: center; gap: 10px;
  }
  .contact__icon { width: 16px; height: 16px; flex: none; }
  .feature-grid {
    position: absolute; left: 110px; top: 262px; width: 700px;
    display: grid; grid-template-columns: repeat(3, 1fr); row-gap: 22px;
  }
  .feature-grid li {
    font-size: 21px; font-weight: 500;
    display: flex; align-items: center; gap: 12px;
  }
  .giveaway {
    position: absolute; left: 60px; top: 394px; width: 730px; height: 38px;
    display: flex; align-items: center; justify-content: space-between;
    font-size: 19px; font-weight: 700; letter-spacing: 0.5px;
  }
  .giveaway__star { width: 18px; height: 18px; }
  .social-line {
    position: absolute; left: 40px; top: 440px; width: 820px; height: 46px;
    display: flex; align-items: center; gap: 18px;
    font-size: 16px; font-weight: 500;
  }
  .social-line__handle { display: flex; align-items: center; gap: 10px; font-size: 20px; }
  .social-line__dot {
    width: 16px; height: 16px; border: 2px solid var(--text-white); border-radius: 50%;
  }
</style>
</head>
<body>

<section class="card card--front" aria-label="Card front">
  <svg class="card__shapes" width="900" height="514" viewBox="0 0 900 514">
    <defs>
      <linearGradient id="photoTones" x1="0" y1="0" x2="1" y2="1">
        <stop offset="0" stop-color="#3b3632"/>
        <stop offset="0.35" stop-color="#d23a86"/>
        <stop offset="0.6" stop-color="#b7b2ad"/>
        <stop offset="1" stop-color="#4f7a3a"/>
      </linearGradient>
    </defs>
    <rect x="0" y="0" width="900" height="514" fill="url(#photoTones)" role="img"
          aria-label="Photo of a young girl tending leafy greens growing in a kitchen grow tower"/>
    <polygon points="0,385 520,385 470,465 0,465" fill="var(--band-dark)" opacity="0.88"/>
    <polygon points="640,0 900,0 900,514 368,514 648,134" fill="#ffffff"/>
    <polygon points="652,0 900,0 900,514 392,514 668,130" fill="var(--brand-blue)"/>
  </svg>
  <p class="tagline">FOOD GROWING MACHINES</p>
  <p class="brand-name">Brightleaf<br>Plots</p>
  <ul class="feature-list feature-list--front">
    <li>Aeroponics Technology <span class="leaf"></span></li>
    <li>No Soil <span class="leaf"></span></li>
    <li>No Pesticides <span class="leaf"></span></li>
    <li>98% Less Water <span class="leaf"></span></li>
    <li>Grow Year Round <span class="leaf"></span></li>
  </ul>
</section>

<section class="card card--back" aria-label="Card back">
  <svg class="card__shapes" width="900" height="514" viewBox="0 0 900 514">
    <line x1="445" y1="40" x2="445" y2="215" stroke="var(--rule)" stroke-width="1.5"/>
    <line x1="60" y1="232" x2="870" y2="232" stroke="var(--rule)" stroke-width="1.5"/>
    <line x1="60" y1="380" x2="870" y2="380" stroke="var(--rule)" stroke-width="1.5"/>
    <polygon points="40,392 800,392 820,434 40,434" fill="var(--band-blue)"/>
    <rect x="0" y="438" width="900" height="50" fill="var(--band-dark)"/>
  </svg>

  <p class="brand-name">Brightleaf<br>Plots</p>

  <div class="contact">
    <p class="contact__name">Chef Morv</p>
    <p class="contact__line">
      <svg class="contact__icon" viewBox="0 0 24 24"><path fill="var(--leaf-green)" d="M6.6 10.8a15 15 0 0 0 6.6 6.6l2.2-2.2a1 1 0 0 1 1-.25 11.4 11.4 0 0 0 3.6.57 1 1 0 0 1 1 1V20a1 1 0 0 1-1 1A17 17 0 0 1 3 4a1 1 0 0 1 1-1h3.5a1 1 0 0 1 1 1c0 1.25.2 2.450.57 3.57a1 1 0 0 1-.25 1z"/></svg>
      555 - 417 - 3290
    </p>
    <p class="contact__line">
      <svg class="contact__icon" viewBox="0 0 24 24"><circle cx="12" cy="12" r="9" fill="none" stroke="var(--leaf-green)" stroke-width="2"/><path d="M3 12h18M12 3c3 3 3 15 0 18M12 3c-3 3-3 15 0 18" fill="none" stroke="var(--leaf-green)" stroke-width="1.6"/></svg>
      www.brightleafplots.example
    </p>
  </div>

  <ul class="feature-list feature-grid">
    <li><span class="leaf"></span>Vertical Farming</li>
    <li><span class="leaf"></span>Urban Farming</li>
    <li><span class="leaf"></span>100% Organic</li>
    <li><span class="leaf"></span>Grows 40% Faster</li>
    <li><span class="leaf"></span>Indoors / Outdoors</li>
  </ul>

  <p class="giveaway">
    <svg class="giveaway__star" viewBox="0 0 24 24"><path fill="#fff" d="M12 2l3 7 7 .6-5.3 4.6 1.6 7.3L12 17.8 5.7 21.5l1.6-7.3L2 9.6 9 9z"/></svg>
    EVERY MONTH ONE SPIRE PLANTER WILL BE GIVEN AWAY
    <svg class="giveaway__star" viewBox="0 0 24 24"><path fill="#fff" d="M12 2l3 7 7 .6-5.3 4.6 1.6 7.3L12 17.8 5.7 21.5l1.6-7.3L2 9.6 9 9z"/></svg>
  </p>

  <p class="social-line">
    <span>* FOLLOW US ON IG FOR A CHANCE TO WIN A SPIRE PLANTER *</span>
    <span class="social-line__handle"><span class="social-line__dot"></span>brightleafplotsxy</span>
  </p>
</section>

</body>
</html>
```